Downtown hair salon need trendy website

I need a website with style. Unique. We need this site to list prices , Hair and nail services, service providers hours. I would also like my logo design on the website. We are located Downtown Grand rapids. Beautiful city with lots of culture.

Target Market(s)

Men and women

Industry/Entity Type

Hair And Beauty

Coding

Coded - Design and coding required

Number of Pages Required

3 page

Font styles to use
Sans Serif

Colors

Designer to choose colors to be used in the design.

Requirements
Must have
• Logo of business. Hours, services and prices, Page for pictures of each service provider. Nail service and prices. Products that we carry... Area on page for my mission statement.
Nice to have
• Pictures of trendy of the beauty industry. Men and women cuts.. Nails..
Should not have
• booking on line options...

```html
<!DOCTYPE html>
<html lang="en">
<head>
<meta charset="utf-8">
<title>Vellora Downtown — Hair &amp; Nail Salon</title>
<link rel="stylesheet" href="https://fonts.googleapis.com/css2?family=Josefin+Sans:wght@300;400;600&family=Montserrat:wght@400;500;600;700&display=swap">
<style>
:root{
  --gold:#b5862c;
  --ink:#222222;
  --muted:#6b6b6b;
  --darker:#141414;
  --white:#ffffff;
  --line:#e4e4e4;
}
*{box-sizing:border-box;margin:0;padding:0}
html,body{width:1200px;height:4859px;overflow:hidden}
body{font-family:"Montserrat",sans-serif;color:var(--ink);background:var(--white);position:relative}
.section{position:relative;width:1200px;overflow:hidden}
.abs{position:absolute}
.heading{font-family:"Josefin Sans",sans-serif;font-weight:300;color:var(--gold);text-transform:uppercase;letter-spacing:1px;white-space:nowrap}
.btn{position:absolute;display:flex;align-items:center;justify-content:center;font-family:"Josefin Sans",sans-serif;font-size:19px;text-transform:uppercase;letter-spacing:.5px;border-radius:5px;white-space:nowrap}
.btn--solid{background:var(--gold);color:var(--white)}
.btn--outline{border:2px solid var(--white);color:var(--white)}
.photo{position:absolute}

/* top bar */
.topbar{height:42px;background:var(--gold)}
.topbar__social{left:76px;top:7px;display:flex;gap:8px}
.dot{width:28px;height:28px;border-radius:50%;background:var(--darker)}
.topbar__hours{right:240px;top:13px;font-size:14px;color:var(--white);white-space:nowrap}
.topbar__phone{left:970px;top:5px;display:flex;align-items:center;gap:10px;color:var(--white);font-family:"Josefin Sans",sans-serif;font-size:21px;white-space:nowrap}
.phone-icon{width:30px;height:30px;border-radius:50%;background:var(--darker);display:flex;align-items:center;justify-content:center}

/* nav */
.nav{height:83px;background:var(--white)}
.nav__link{top:32px;font-size:14px;color:#555;text-transform:uppercase}
.nav__link--active{left:219px;top:20px;width:84px;height:42px;background:var(--gold);color:var(--white);border-radius:4px;display:flex;align-items:center;justify-content:center}
.brand{left:500px;top:0;width:200px;height:83px;display:flex;flex-direction:column;align-items:center;justify-content:flex-end;padding-bottom:10px}
.brand__mark{width:36px;height:36px;border-radius:50%;border:2px solid var(--gold);margin-bottom:4px}
.brand__name{font-family:"Josefin Sans",sans-serif;font-size:26px;color:var(--gold);letter-spacing:1px}

/* hero */
.hero{height:552px;background:linear-gradient(90deg,#f6f1e8 0%,#f3ece0 55%,#eee4d6 100%)}
.hero__photo{right:0;top:0;width:560px;height:552px;background:radial-gradient(ellipse at 55% 45%,#c9a48a 0%,#7a5646 35%,#3b2a24 60%,rgba(238,228,214,0) 78%)}
.hero__kicker{left:108px;top:172px;font-family:"Josefin Sans",sans-serif;font-size:29px;color:#2a2a2a}
.hero__title{left:107px;top:210px;font-family:"Josefin Sans",sans-serif;font-weight:600;font-size:51px;color:#2a2a2a;letter-spacing:-.5px;white-space:nowrap}
.hero__sub{left:108px;top:268px;font-family:"Josefin Sans",sans-serif;font-size:29px;color:#2a2a2a}
.hero__sub b{color:var(--gold);font-weight:600}
.hero__btn{left:108px;top:318px;width:271px;height:51px}
.hero__arrow{top:234px;width:48px;height:48px;border-radius:50%;background:var(--white);display:flex;align-items:center;justify-content:center}

/* services strip */
.services{height:339px;background:var(--darker)}
.service{top:0;width:400px;height:339px}
.service--hair{left:0;background:linear-gradient(135deg,#3a3532,#1c1a19 60%,#2a2522)}
.service--nail{left:800px;background:linear-gradient(135deg,#2a0f12,#5a1a22 45%,#1a1012)}
.service__frame{left:21px;top:22px;width:356px;height:297px;border:1px solid rgba(255,255,255,.35)}
.service__title{left:0;width:400px;top:134px;text-align:center;font-weight:700;font-size:31px;color:var(--white);font-family:"Josefin Sans",sans-serif}
.service__text{left:0;width:400px;top:176px;text-align:center;font-size:14px;color:var(--white)}
.service--main{left:400px;background:var(--gold)}
.service--main .heading{color:var(--white);font-size:40px;left:0;width:400px;text-align:center;top:78px}
.service__desc{left:58px;width:284px;top:132px;text-align:center;color:var(--white);font-size:13.5px;line-height:27px}
.service__btn{left:64px;top:203px;width:270px;height:50px}
.badge{left:545px;top:565px;width:100px;height:100px;border-radius:50%;background:var(--white);border:6px solid #f1e6d4;z-index:2}

/* mission */
.mission{height:649px;background:var(--white)}
.mission .heading{left:0;width:1200px;text-align:center;top:60px;font-size:42px}
.mission__sub{left:0;width:1200px;text-align:center;top:114px;font-weight:600;font-size:14px;letter-spacing:.5px}
.mission__quote{left:298px;width:604px;top:156px;text-align:center;font-style:italic;font-size:14px;line-height:27px;color:#444}
.mission__photo{left:311px;top:249px;width:576px;height:400px;background:radial-gradient(ellipse at 50% 55%,#f3ddd0 0%,#eed3c3 40%,rgba(255,255,255,0) 72%)}

/* pricing */
.pricing{height:761px;background:linear-gradient(180deg,#2a2a2a,#1b1b1b)}
.pricing .heading{left:0;width:1200px;text-align:center;top:58px;font-size:45px}
.pricing__intro{left:290px;width:620px;top:114px;text-align:center;font-size:14px;line-height:27px;color:#ddd}
.pricing__card{left:106px;top:196px;width:988px;height:500px;background:var(--white)}
.tabs{left:258px;top:0;display:flex}
.tab{width:234px;height:63px;display:flex;align-items:center;justify-content:center;font-family:"Josefin Sans",sans-serif;font-size:18px;text-transform:uppercase}
.tab--active{background:var(--gold);color:var(--white)}
.tab--idle{border:2px solid var(--gold);color:var(--gold)}
.price-col{top:110px;width:400px}
.price-col--man{left:41px}
.price-col--woman{left:532px}
.price-col__title{font-family:"Josefin Sans",sans-serif;font-weight:600;font-size:22px;color:var(--gold);margin-bottom:20px}
.price-row{height:64px}
.price-row__line{display:flex;font-weight:600;font-size:15px;color:var(--ink);align-items:baseline;white-space:nowrap}
.price-row__dots{flex:1;border-bottom:2px dotted #777;margin:0 3px;transform:translateY(-3px)}
.price-row__time{font-size:13px;color:var(--muted);margin-top:6px}
.price-row--highlight .price-row__line{color:var(--gold)}
.price-row--highlight .price-row__dots{border-color:var(--gold)}
.price-divider{left:494px;top:110px;width:1px;height:360px;background:var(--line)}

/* products */
.products{height:617px;background:var(--white)}
.products__ring{border-radius:50%;border:1.5px solid #e6cfa8}
.products__photo{left:255px;top:56px;width:190px;height:510px;background:linear-gradient(180deg,#2a4c86,#1b3566 50%,#142a55);border-radius:26px 26px 10px 10px}
.products .heading{left:655px;top:100px;font-size:43px}
.products__sub{left:659px;top:150px;font-weight:700;font-size:14px;letter-spacing:1px}
.products__text{left:659px;width:380px;font-size:13px;line-height:27px;color:#555}
.products__btn{left:658px;top:462px;width:270px;height:49px}

/* team */
.team{height:572px;background:linear-gradient(90deg,#f3ebe0,#f7f1e8 60%,#efe4d4)}
.team__hand{left:30px;top:60px;width:280px;height:360px;background:radial-gradient(ellipse,#efdfcf 0%,rgba(247,241,232,0) 70%)}
.team__photo{left:943px;top:0;width:257px;height:572px;background:radial-gradient(ellipse at 60% 40%,#d9ab8e 0%,#6b3a28 30%,#3a1f16 55%,rgba(239,228,212,0) 85%)}
.team .heading{left:0;width:1200px;text-align:center;top:74px;font-size:43px}
.team__intro{left:330px;width:540px;top:134px;text-align:center;font-size:13px;line-height:27px;color:#555}
.stylists{left:294px;top:205px;width:595px;display:flex;gap:16px}
.stylist{width:188px;background:var(--white);border:1px solid var(--line)}
.stylist__photo{height:150px}
.stylist__body{padding:10px 12px 12px;text-align:center}
.stylist__name{font-weight:600;font-size:14px;color:var(--ink)}
.stylist__role{font-size:12px;color:var(--gold);margin-top:3px}
.stylist__hours{font-size:11.5px;color:var(--muted);margin-top:5px}
.team__btn{left:464px;top:447px;width:270px;height:51px}

/* follow */
.follow{height:901px;background:var(--white)}
.follow .heading{left:0;width:1200px;text-align:center;top:68px;font-size:43px}
.follow__icon{left:586px;top:125px;width:28px;height:28px;border-radius:6px;background:var(--gold)}
.tile{width:270px;height:270px}
.follow__btn{left:521px;top:784px;width:158px;height:47px}

/* footer */
.footer{height:344px;background:linear-gradient(90deg,#121212,#1f1f1f 60%,#191919)}
.footer__brand{left:138px;top:88px;width:192px;display:flex;flex-direction:column;align-items:center;gap:10px}
.footer__brand .brand__mark{width:56px;height:56px;margin:0}
.footer__brand .brand__name{font-size:38px}
.footer__col{top:40px}
.footer__title{font-family:"Josefin Sans",sans-serif;font-size:15px;font-weight:400;color:var(--gold);text-transform:uppercase;margin-bottom:16px}
.footer__list{list-style:none}
.footer__list li{font-size:13px;color:#d8d8d8;height:29px;display:flex;align-items:center;gap:12px;white-space:nowrap}
.footer__list li::before{content:"";width:6px;height:6px;border-radius:50%;background:var(--gold)}
.contact-row{display:flex;gap:16px;font-size:13px;color:#d8d8d8;line-height:22px;margin-bottom:14px}
.footer__social{display:flex;gap:10px;margin-top:4px}
.footer__social .dot{width:38px;height:38px;background:#2b5fb8}
.footer__social .dot:nth-child(2){background:#6a8fbd}
.footer__social .dot:nth-child(3){background:#2a9de0}
.footer__copy{left:0;width:1200px;top:302px;text-align:center;font-size:13px;color:#bbb}
</style>
</head>
<body>

<header class="section topbar">
  <div class="abs topbar__social"><span class="dot"></span><span class="dot"></span><span class="dot"></span></div>
  <span class="abs topbar__hours">Open Tue – Sat 9am – 7pm</span>
  <div class="abs topbar__phone">
    <span class="phone-icon"><svg width="16" height="16" viewBox="0 0 24 24"><path fill="#fff" d="M6.6 10.8a15 15 0 0 0 6.6 6.6l2.2-2.2c.3-.3.7-.4 1-.2 1.1.4 2.3.6 3.6.6.6 0 1 .4 1 1V20c0 .6-.4 1-1 1A17 17 0 0 1 3 4c0-.6.4-1 1-1h3.5c.6 0 1 .4 1 1 0 1.3.2 2.5.6 3.6.1.3 0 .7-.2 1z"/></svg></span>
    555 218 4630
  </div>
</header>

<nav class="section nav">
  <span class="abs nav__link nav__link--active">Home</span>
  <span class="abs nav__link" style="left:333px">About</span>
  <span class="abs nav__link" style="left:416px">Services</span>
  <div class="abs brand"><span class="brand__mark"></span><span class="brand__name">VELLORA</span></div>
  <span class="abs nav__link" style="left:708px">Products</span>
  <span class="abs nav__link" style="left:819px">Team</span>
  <span class="abs nav__link" style="left:916px">Contact</span>
</nav>

<section class="section hero">
  <div class="photo hero__photo" role="img" aria-label="Smiling woman with a glossy brown bob haircut"></div>
  <p class="abs hero__kicker">THE BEST</p>
  <h1 class="abs hero__title">PROFESSIONAL CARE</h1>
  <p class="abs hero__sub">FOR <b>YOUR HAIR &amp; NAIL</b></p>
  <a class="btn btn--solid hero__btn">View Our Prices</a>
  <span class="abs hero__arrow" style="left:14px"><svg width="14" height="20" viewBox="0 0 14 20"><path d="M11 2 3 10l8 8" fill="none" stroke="#b5862c" stroke-width="1.5"/></svg></span>
  <span class="abs hero__arrow" style="left:1136px"><svg width="14" height="20" viewBox="0 0 14 20"><path d="m3 2 8 8-8 8" fill="none" stroke="#b5862c" stroke-width="1.5"/></svg></span>
</section>

<section class="section services">
  <div class="abs service service--hair" role="img" aria-label="Barber styling a man's hair">
    <div class="abs service__frame"></div>
    <h3 class="abs service__title">HAIR CUT</h3>
    <p class="abs service__text">Lorem Ipsum is simply text</p>
  </div>
  <div class="abs service service--main">
    <h2 class="abs heading">Our Services</h2>
    <p class="abs service__desc">Lorem Ipsum is simply dummy text of the printing and typesetting industry</p>
    <a class="btn btn--outline service__btn">View Services</a>
  </div>
  <div class="abs service service--nail" role="img" aria-label="Red lips and glitter-painted nails">
    <div class="abs service__frame"></div>
    <h3 class="abs service__title">NAIL CUT</h3>
    <p class="abs service__text">Lorem Ipsum is simply text</p>
  </div>
</section>
<span class="abs badge"></span>

<section class="section mission">
  <h2 class="abs heading">Our Mission</h2>
  <p class="abs mission__sub">VELLORA DOWNTOWN</p>
  <p class="abs mission__quote">" Lorem Ipsum is simply dummy text of the printing and typesetting industry. Lorem Ipsum has been the industry's standard dummy text ever since the 1500s, when an unknown printer took a galley of type and scrambled "</p>
  <div class="photo mission__photo" role="img" aria-label="Hands filing manicured nails with a white nail file"></div>
</section>

<section class="section pricing">
  <h2 class="abs heading">Plan and Pricing</h2>
  <p class="abs pricing__intro">" Lorem Ipsum is simply dummy text of the printing and typesetting industry Lorem Ipsum has been the industry's standard dummy text ever since.</p>
  <div class="abs pricing__card">
    <div class="abs tabs"><span class="tab tab--active">Nail Cuts</span><span class="tab tab--idle">Hair Cuts</span></div>
    <div class="abs price-col price-col--man">
      <h3 class="price-col__title">MAN</h3>
      <div class="price-row"><div class="price-row__line">Lorem ipsum simple text<span class="price-row__dots"></span>$20</div><p class="price-row__time">1 hours</p></div>
      <div class="price-row price-row--highlight"><div class="price-row__line">Lorem ipsum simple text<span class="price-row__dots"></span>$20</div><p class="price-row__time">1 hours</p></div>
      <div class="price-row"><div class="price-row__line">Lorem ipsum simple text<span class="price-row__dots"></span>$20</div><p class="price-row__time">1 hours</p></div>
      <div class="price-row"><div class="price-row__line">Lorem ipsum simple text<span class="price-row__dots"></span>$20</div><p class="price-row__time">1 hours</p></div>
      <div class="price-row"><div class="price-row__line">Lorem ipsum simple text<span class="price-row__dots"></span>$20</div><p class="price-row__time">1 hours</p></div>
    </div>
    <span class="abs price-divider"></span>
    <div class="abs price-col price-col--woman">
      <h3 class="price-col__title">WOMAN</h3>
      <div class="price-row"><div class="price-row__line">Lorem ipsum simple text<span class="price-row__dots"></span>$20</div><p class="price-row__time">1 hours</p></div>
      <div class="price-row"><div class="price-row__line">Lorem ipsum simple text<span class="price-row__dots"></span>$20</div><p class="price-row__time">1 hours</p></div>
      <div class="price-row"><div class="price-row__line">Lorem ipsum simple text<span class="price-row__dots"></span>$20</div><p class="price-row__time">1 hours</p></div>
      <div class="price-row"><div class="price-row__line">Lorem ipsum simple text<span class="price-row__dots"></span>$20</div><p class="price-row__time">1 hours</p></div>
      <div class="price-row"><div class="price-row__line">Lorem ipsum simple text<span class="price-row__dots"></span>$20</div><p class="price-row__time">1 hours</p></div>
    </div>
  </div>
</section>

<section class="section products">
  <span class="abs products__ring" style="left:122px;top:95px;width:440px;height:440px"></span>
  <span class="abs products__ring" style="left:162px;top:135px;width:360px;height:360px"></span>
  <div class="photo products__photo" role="img" aria-label="Blue bottles of professional hair care product"></div>
  <h2 class="abs heading">Products</h2>
  <p class="abs products__sub">WE CARRY</p>
  <p class="abs products__text" style="top:196px">Lorem Ipsum is simply dummy text of the printing and typesetting industry. Lorem Ipsum has been the industry's standard dummy text ever since the 1500s, when an unknown printer took a galley of type and scrambled it to make a type specimen book.</p>
  <p class="abs products__text" style="top:342px">Lorem Ipsum is simply dummy text of the printing and typesetting industry. Lorem Ipsum has been the industry's standard dummy text ever since the 1500s, when an unknown printer took a galley</p>
  <a class="btn btn--solid products__btn">View Products</a>
</section>

<section class="section team">
  <div class="photo team__hand" role="img" aria-label="Faint image of a manicured hand"></div>
  <div class="photo team__photo" role="img" aria-label="Woman with long glossy auburn hair"></div>
  <h2 class="abs heading">Meet Our Stylists</h2>
  <p class="abs team__intro">Lorem Ipsum is simply dummy text of the printing and typesetting industry. Lorem Ipsum has been the industry's standard dummy</p>
  <div class="abs stylists">
    <div class="stylist">
      <div class="stylist__photo" role="img" aria-label="Portrait of hair stylist Mara Quinn" style="background:linear-gradient(160deg,#d8c2ad,#8a5a44)"></div>
      <div class="stylist__body"><p class="stylist__name">Mara Quinn</p><p class="stylist__role">Hair Stylist</p><p class="stylist__hours">Tue – Fri · 9am – 5pm</p></div>
    </div>
    <div class="stylist">
      <div class="stylist__photo" role="img" aria-label="Portrait of barber Theo Lang" style="background:linear-gradient(160deg,#cfcfcf,#4a3a32)"></div>
      <div class="stylist__body"><p class="stylist__name">Theo Lang</p><p class="stylist__role">Barber</p><p class="stylist__hours">Wed – Sat · 10am – 7pm</p></div>
    </div>
    <div class="stylist">
      <div class="stylist__photo" role="img" aria-label="Portrait of nail technician Ivy Carter" style="background:linear-gradient(160deg,#e6ccc4,#8a2232)"></div>
      <div class="stylist__body"><p class="stylist__name">Ivy Carter</p><p class="stylist__role">Nail Technician</p><p class="stylist__hours">Tue – Sat · 9am – 6pm</p></div>
    </div>
  </div>
  <a class="btn btn--solid team__btn">View All Stylists</a>
</section>

<section class="section follow">
  <h2 class="abs heading">Follow Us On</h2>
  <span class="abs follow__icon"></span>
  <div class="abs tile" style="left:174px;top:199px;background:linear-gradient(135deg,#4a5aa0,#e4c8b4 45%,#c84a8a)" role="img" aria-label="Floral nail art on fingertips"></div>
  <div class="abs tile" style="left:466px;top:199px;background:linear-gradient(160deg,#6a6a6a,#2e2a28 60%,#bdbdbd)" role="img" aria-label="Woman with flowing dark hair"></div>
  <div class="abs tile" style="left:757px;top:199px;background:linear-gradient(135deg,#e8d8d4,#b0303a 50%,#e6d2cc)" role="img" aria-label="Red lips and glitter nails"></div>
  <div class="abs tile" style="left:174px;top:492px;background:linear-gradient(135deg,#4a6a60,#c8b2a0 50%,#3a4a44)" role="img" aria-label="Hand with black painted nails"></div>
  <div class="abs tile" style="left:466px;top:492px;background:linear-gradient(180deg,#d8d8d8,#8a7060 50%,#b03030)" role="img" aria-label="Bearded man portrait"></div>
  <div class="abs tile" style="left:757px;top:492px;background:linear-gradient(135deg,#3a0a14,#8a1e2e 50%,#2a0810)" role="img" aria-label="Woman with long red hair"></div>
  <a class="btn btn--solid follow__btn">View More</a>
</section>

<footer class="section footer">
  <div class="abs footer__brand"><span class="brand__mark"></span><span class="brand__name">VELLORA</span></div>
  <div class="abs footer__col" style="left:438px">
    <h4 class="footer__title">Sitemap</h4>
    <ul class="footer__list"><li>Home</li><li>About</li><li>Services</li><li>Products</li><li>Team</li><li>Contact</li></ul>
  </div>
  <div class="abs footer__col" style="left:638px">
    <h4 class="footer__title">Services</h4>
    <ul class="footer__list"><li>Man Hair cut</li><li>Man nail cut</li><li>Woman Hair cut</li><li>Woman nail cut</li></ul>
  </div>
  <div class="abs footer__col" style="left:855px;width:230px">
    <h4 class="footer__title">Contact Us</h4>
    <div class="contact-row"><svg width="16" height="16" viewBox="0 0 24 24"><path fill="#b5862c" d="M6.6 10.8a15 15 0 0 0 6.6 6.6l2.2-2.2c.3-.3.7-.4 1-.2 1.1.4 2.3.6 3.6.6.6 0 1 .4 1 1V20c0 .6-.4 1-1 1A17 17 0 0 1 3 4c0-.6.4-1 1-1h3.5c.6 0 1 .4 1 1 0 1.3.2 2.5.6 3.6.1.3 0 .7-.2 1z"/></svg>+(1) 555 218 4630</div>
    <div class="contact-row"><svg width="16" height="14" viewBox="0 0 16 12"><rect width="16" height="12" fill="#b5862c"/><path d="m0 0 8 6 8-6" fill="none" stroke="#1b1b1b" stroke-width="1.2"/></svg>info@vellorasalon.com</div>
    <div class="contact-row"><svg width="16" height="20" viewBox="0 0 16 20"><path fill="#b5862c" d="M8 0a7 7 0 0 0-7 7c0 5 7 13 7 13s7-8 7-13a7 7 0 0 0-7-7zm0 10a3 3 0 1 1 0-6 3 3 0 0 1 0 6z"/></svg><span>101 - Lorem ipsum simple<br>text print industry</span></div>
    <div class="footer__social"><span class="dot"></span><span class="dot"></span><span class="dot"></span></div>
  </div>
  <p class="abs footer__copy">©VELLORA DOWNTOWN -2019 All Rights Reserved.</p>
</footer>

</body>
</html>
```